Fresh Rally Quest

I need a design for and advertisement on a Screen at a Doctor's Surgery. The ad would be up for 15 seconds then on a rotation which last 10 minutes. So every 10 minutes if you are sitting in the Doctor's waiting room you will see my ad for 15 seconds.

I am a Personal Trainer and my company is TrueForm Habits. I need this advertisement for my January promotion, I will be running the ad in December. So I need the ad to send to the agent by this Friday.

I attach something for you to start with, basically person sitting in the doctor's waiting room must see headline, value of offer discounted price and webpage. The rest of the stuff should be on ad for those sitting in the waiting room for a long time.

This is a really important ad as January is the biggest month for Personal Trainers, I can't mess this up

Reason: So I've decided it makes sense to split the project into two, one for the screen, and then the full ad as you have it to fit on an A6 post card. So here are some update: Phone number should be written as (07482) 315907 Change spelling of Program to Programme (£600 Value) change to (Value £600) (£25) Value change to (Value £25) (£45 Value) change to (Value £45) For the screen replace the woman with my picture Also I just got this width to height ratio of the screen is 16:9 The important things to call out on the screen "Early Bird Offer Custom Kick Start Program" "Who Wants To Lose 15 Pounds and Be Healthy in 2015" The Cost of £200 The Savings of £470 The Expiration Date Limited to Fist 10 Individuals Enroll Now The screen should also tell people to pick up a flyer in the Waiting Room Then the flyer, remember just A6 post card should have the full Ad Thank you for taking the time to design my ad

Use colors in my logo. Important for the screen: So I've decided it makes sense to split the project into two, one for the screen, and then the full ad as you have it to fit on an A6 post card. So here are some update: Phone number should be written as (07482) 315907 Change spelling of Program to Programme (£600 Value) change to (Value £600) (£25) Value change to (Value £25) (£45 Value) change to (Value £45) For the screen replace the woman with my picture Also I just got this width to height ratio of the screen is 16:9 The important things to call out on the screen "Early Bird Offer Custom Kick Start Program" "Who Wants To Lose 15 Pounds and Be Healthy in 2015" Cost of £200 Savings of £470 The Expiration Date Limited to First 10 Individuals Enroll Now The screen should also tell people to pick up a flyer in the Waiting Room Then the flyer, remember just A6 post card should have the full Ad Thank you for taking the time to design my ad

Women in the age group of 25 to 60, who want to get strong and fit, but are afraid of the weight room. So measure about strength must be subtle or just not there at all. This is not a call for bodybuilders

• Use colors in my logo. Important for the screen:

So I've decided it makes sense to split the project into two, one for the screen, and then the full ad as you have it to fit on an A6 post card.

So here are some update:

Phone number should be written as (07482) 315907
Change spelling of Program to Programme
(£600 Value) change to (Value £600)
(£25) Value change to (Value £25)
(£45 Value) change to (Value £45)
For the screen replace the woman with my picture

Also I just got this width to height ratio of the screen is 16:9

The important things to call out on the screen
"Early Bird Offer Custom Kick Start Program"
"Who Wants To Lose 15 Pounds and Be Healthy in 2015"
The Cost of £200
The Savings of £470
The Expiration Date
Limited to Fist 10 Individuals
Enroll Now

The screen should also tell people to pick up a flyer in the Waiting Room

Then the flyer, remember just A6 post card should have the full Ad

Thank you for taking the time to design my ad

```html
<!DOCTYPE html>
<html lang="en">
<head>
<meta charset="utf-8">
<title>TrueForm Habits – Fresh Rally Quest Screen Ad</title>
<link href="https://fonts.googleapis.com/css2?family=Open+Sans:wght@400;700;800&display=swap" rel="stylesheet">
<style>
  :root {
    --bg-centre: #2a8fe6;
    --bg-mid: #0d5bb0;
    --bg-edge: #05204a;
    --text-white: #ffffff;
    --price-yellow: #fff200;
    --burst-orange: #fc9b1c;
    --burst-text: #2b1a05;
    --brand-blue: #2aa3ea;
    --frame-white: #ffffff;
    --photo-warm: #b98a6a;
    --photo-dark: #3a3b40;
  }
  * { margin: 0; padding: 0; box-sizing: border-box; }
  html, body { width: 1200px; height: 734px; overflow: hidden; }
  body { font-family: "Open Sans", Arial, sans-serif; }

  .ad-screen {
    position: relative;
    width: 1200px;
    height: 734px;
    overflow: hidden;
    background: radial-gradient(ellipse 70% 80% at 58% 48%, var(--bg-centre) 0%, var(--bg-mid) 45%, var(--bg-edge) 100%);
    color: var(--text-white);
  }

  .headline {
    position: absolute;
    left: 60px;
    top: 24px;
    width: 800px;
    text-align: center;
    white-space: nowrap;
  }
  .headline-offer { font-weight: 800; font-size: 29px; line-height: 1.2; color: var(--price-yellow); }
  .headline-question { font-weight: 700; font-size: 23px; line-height: 1.3; margin-top: 4px; }

  .brand {
    position: absolute;
    left: 118px;
    top: 140px;
    display: flex;
    align-items: center;
    gap: 12px;
  }
  .brand-dot {
    width: 28px; height: 28px;
    border-radius: 50%;
    background: var(--brand-blue);
  }
  .brand-name {
    font-weight: 800;
    font-size: 34px;
    color: var(--text-white);
    letter-spacing: -0.5px;
  }

  .trainer-photo {
    position: absolute;
    left: 88px;
    top: 253px;
    width: 275px;
    height: 368px;
    border: 6px solid var(--frame-white);
    background: linear-gradient(160deg, var(--photo-dark) 0%, var(--photo-warm) 55%, #e8685f 100%);
  }

  .savings-burst {
    position: absolute;
    left: 865px;
    top: 75px;
    width: 200px;
    height: 190px;
  }
  .savings-burst svg { width: 100%; height: 100%; display: block; }
  .savings-text {
    position: absolute;
    inset: 0;
    display: flex;
    flex-direction: column;
    align-items: center;
    justify-content: center;
    transform: rotate(-22deg);
    color: var(--burst-text);
    font-weight: 800;
    font-size: 30px;
    line-height: 1.05;
  }

  .offer {
    position: absolute;
    left: 380px;
    width: 760px;
    text-align: center;
    white-space: nowrap;
  }
  .offer-limit { top: 246px; font-weight: 800; font-size: 41px; }
  .offer-enroll { top: 304px; font-weight: 800; font-size: 39px; left: 365px; }
  .offer-enroll .only { color: var(--price-yellow); font-size: 36px; margin-left: 10px; }
  .offer-enroll .price { color: var(--price-yellow); font-size: 56px; line-height: 1; }
  .offer-call { top: 380px; font-weight: 700; font-size: 30px; }
  .offer-phone { top: 422px; font-weight: 800; font-size: 56px; letter-spacing: 1px; }
  .offer-or { top: 510px; font-weight: 400; font-size: 37px; }
  .offer-url { top: 563px; font-weight: 800; font-size: 24px; }
  .offer-bonus { top: 601px; font-weight: 700; font-size: 21px; }

  .footer-note {
    position: absolute;
    left: 0;
    top: 664px;
    width: 1200px;
    text-align: center;
    font-weight: 700;
    font-size: 23px;
  }
  .footer-note .expiry { color: var(--price-yellow); }
</style>
</head>
<body>
  <main class="ad-screen">
    <header class="headline">
      <h1 class="headline-offer">Early Bird Offer – Custom Kick Start Programme</h1>
      <p class="headline-question">Who Wants To Lose 15 Pounds and Be Healthy in 2015?</p>
    </header>

    <div class="brand">
      <span class="brand-dot"></span>
      <span class="brand-name">TrueForm Habits</span>
    </div>

    <div class="trainer-photo" role="img" aria-label="Portrait photo of Dana, the personal trainer, smiling in a gym wearing a coral vest"></div>

    <div class="savings-burst">
      <svg viewBox="0 0 200 200" aria-hidden="true">
        <polygon fill="var(--burst-orange)" points="100,8 116,40 146,20.3 143.8,56.2 179.7,54 159.9,83.9 192,100 159.9,116.1 179.7,146 143.8,143.8 146,179.7 116,159.9 100,192 84,159.9 54,179.7 56.2,143.8 20.3,146 40.1,116.1 8,100 40.1,83.9 20.3,54 56.2,56.2 54,20.3 84,40"/>
      </svg>
      <div class="savings-text"><span>Save</span><span>£470</span></div>
    </div>

    <p class="offer offer-limit">Limited To The First 10 Individuals</p>
    <p class="offer offer-enroll">To Enroll Now <span class="only">Only</span> <span class="price">£200</span></p>
    <p class="offer offer-call">Call and Ask for Dana (that’s me in the picture)</p>
    <p class="offer offer-phone">(07482) 315907</p>
    <p class="offer offer-or">or visit</p>
    <p class="offer offer-url">https://trueformhabits.pagesite.net/fresh-rally-quest/</p>
    <p class="offer offer-bonus">And get the Sexy Stomach Special Report</p>

    <p class="footer-note"><span class="expiry">Offer ends 31 January</span> · Pick up a flyer here in the waiting room</p>
  </main>
</body>
</html>
```